Cardiology Practice needs a Heart Scan Order Form

Busy cardiology practice needs an order form for a heart scan test. Sample is attached. One side should have all information noted and the other side should have our physician names (Dorian Velko, MD, L.N. Morvesti, MD, Ovila Brandt, MD, Tomas Velko, MD, and Gerald Pompetti, MD. It should have the map that is uploaded and our demographic information (Crestfield Cardiac PLLC, 712 Harrow Ln. Ste. K, Melrick, TX 77431 along with phone 832-417-2286 and fax 832-417-2287) as well as our web address (crestfieldcardiac.example). Our primary colors are red, black and white. Needs to fit paper size 8 1/2 by 11.

Target Market(s)

Healthcare

Industry/Entity Type

Health Care

Font styles to use
Serif

Colors
ec1f27

Requirements
Must have
• Logo, information listed on sample form, demographics and physician names as well as website.
Nice to have
• Open to suggestions
Should not have
• Physician Pictures

```html
<!DOCTYPE html>
<html lang="en">
<head>
<meta charset="utf-8">
<title>Crestfield Cardiac – Physicians &amp; Location</title>
<link rel="stylesheet" href="https://fonts.googleapis.com/css2?family=Pathway+Gothic+One&family=Oswald:wght@300;400&family=Archivo+Black&display=swap">
<style>
  :root{
    --red:#c1323b;
    --red-light:#f3a2a2;
    --ink:#111111;
    --divider:#c4c4c4;
    --map-grey:#e8e8e6;
    --map-sand:#f6ecc8;
    --map-pink:#f4d3d3;
    --paper:#ffffff;
  }
  *{margin:0;padding:0;box-sizing:border-box}
  html,body{width:928px;height:1200px;overflow:hidden;background:var(--paper)}
  .sheet{position:relative;width:928px;height:1200px;font-family:"Pathway Gothic One",sans-serif;color:var(--ink)}

  .brand{position:absolute;left:54px;top:86px;display:flex;align-items:center;gap:14px}
  .brand-dot{width:22px;height:22px;border-radius:50%;background:var(--red)}
  .brand-name{font-family:"Archivo Black",sans-serif;font-size:38px;color:var(--red);letter-spacing:1px;line-height:1}

  .rule{position:absolute;left:54px;width:813px;height:6px;background:var(--red)}
  .rule.top{top:212px}
  .rule.bottom{top:1050px;height:5px}

  .heading{position:absolute;display:flex;align-items:center;gap:15px;font-family:"Oswald",sans-serif;font-weight:300;font-size:40px;color:var(--red);line-height:1;letter-spacing:-0.5px}
  .heading::before{content:"";width:0;height:0;border-top:9px solid transparent;border-bottom:9px solid transparent;border-left:14px solid var(--red)}
  .heading.physicians{left:54px;top:249px}
  .heading.nurses{left:471px;top:249px}
  .heading.location{left:54px;top:528px}

  .roster{position:absolute;list-style:none}
  .roster.physicians{left:54px;top:307px}
  .roster.nurses{left:471px;top:307px}
  .roster li{position:relative;height:38px;padding-left:86px;font-size:24px;line-height:28px;white-space:nowrap}
  .roster li::before{content:"";position:absolute;left:0;top:13px;width:60px;height:1px;background:var(--red)}
  .roster li::after{content:"";position:absolute;left:58px;top:7px;width:13px;height:13px;border-radius:50%;background:radial-gradient(circle at 40% 40%,var(--red-light),var(--red) 65%)}
  .roster .cred{font-size:17px}

  .map{position:absolute;left:54px;top:588px;width:813px;height:441px;border-radius:12px;
    background:
      radial-gradient(ellipse 120px 90px at 48% 42%,var(--map-pink),transparent 70%),
      radial-gradient(ellipse 200px 160px at 12% 70%,var(--map-sand),transparent 70%),
      radial-gradient(ellipse 140px 120px at 92% 20%,var(--map-sand),transparent 70%),
      var(--map-grey)}

  .contact{position:absolute;top:1086px;display:flex;align-items:flex-start;gap:9px;font-size:17px;line-height:22px;white-space:nowrap}
  .contact svg{flex:none;fill:var(--red);margin-top:2px}
  .contact.address{left:54px}
  .contact.phone{left:348px}
  .contact.fax{left:527px}
  .contact.web{left:703px}
  .divider{position:absolute;top:1082px;width:1px;height:61px;background:var(--divider)}
  .divider.d1{left:315px}
  .divider.d2{left:489px}
  .divider.d3{left:668px}
</style>
</head>
<body>
<main class="sheet">
  <div class="brand">
    <span class="brand-dot"></span>
    <span class="brand-name">CRESTFIELD CARDIAC</span>
  </div>

  <div class="rule top"></div>

  <h2 class="heading physicians">Our Physicians</h2>
  <ul class="roster physicians">
    <li>Dorian Velko, <span class="cred">M.D.</span></li>
    <li>L.N. Morvesti, <span class="cred">M.D.</span></li>
    <li>Ovila Brandt, <span class="cred">M.D.</span></li>
    <li>Tomas Velko, <span class="cred">M.D.</span></li>
    <li>Gerald Pompetti, <span class="cred">M.D.</span></li>
  </ul>

  <h2 class="heading nurses">Our Nurse Practitioners</h2>
  <ul class="roster nurses">
    <li>Marla Dovensky, <span class="cred">MSN, ACNP-BC</span></li>
    <li>Renna Whitcombe, <span class="cred">MSN, APRN, AGNP-C</span></li>
    <li>Kayla Thorsen, <span class="cred">MSN, APRN, NP-C</span></li>
  </ul>

  <h2 class="heading location">Our Location</h2>
  <div class="map" role="img" aria-label="Street map showing the clinic location marked with a red pin, with the surrounding streets, shops and restaurants"></div>

  <div class="rule bottom"></div>

  <div class="contact address">
    <svg width="14" height="20" viewBox="0 0 14 20"><path d="M7 0C3.1 0 0 3.1 0 7c0 5 7 13 7 13s7-8 7-13c0-3.9-3.1-7-7-7zm0 10a3 3 0 1 1 0-6 3 3 0 0 1 0 6z"/></svg>
    <span>Crestfield Cardiac PLLC located at 712<br>Harrow Ln. Ste. K, Melrick, TX 77431.</span>
  </div>
  <div class="divider d1"></div>
  <div class="contact phone">
    <svg width="16" height="16" viewBox="0 0 24 24"><path d="M6.6 10.8c1.4 2.8 3.8 5.1 6.6 6.6l2.2-2.2c.3-.3.7-.4 1-.2 1.1.4 2.3.6 3.6.6.6 0 1 .4 1 1V20c0 .6-.4 1-1 1C10.6 21 3 13.4 3 4c0-.6.4-1 1-1h3.5c.6 0 1 .4 1 1 0 1.3.2 2.5.6 3.6.1.3 0 .7-.2 1l-2.3 2.2z"/></svg>
    <span>832-417-2286</span>
  </div>
  <div class="divider d2"></div>
  <div class="contact fax">
    <svg width="20" height="18" viewBox="0 0 20 18"><rect x="5" y="0" width="10" height="6"/><rect x="0" y="6" width="20" height="9" rx="2"/><rect x="5" y="12" width="10" height="6" fill="#fff" stroke="#c1323b" stroke-width="1.5"/></svg>
    <span>832-417-2287</span>
  </div>
  <div class="divider d3"></div>
  <div class="contact web">
    <svg width="18" height="14" viewBox="0 0 20 16"><rect x="0" y="0" width="20" height="16" rx="2"/><path d="M1 2l9 7 9-7" fill="none" stroke="#fff" stroke-width="1.5"/></svg>
    <span>www.crestfieldcardiac.example</span>
  </div>
</main>
</body>
</html>
```